App Design for Restaurant App

We need a design for the new Mobile App for the Restaurant Volmik. See attachment for presentation sketches.
There are two attached files: File 2 shows the App in general and File 1 shows the five screens which need to be designed. Your work should contain the general color scheme, icons and layout proposal.
Updates
Hi Designers
There where several questions about the scope of the work. We are looking for a design for an App. The promotion website of the restaurant Volmik can be found under www.restaurant-volmik.ch
There you will get an impression of the Corporate Identity used by the restaurant and you will also find the logo.
In the sketch there are several screens which don't need a design, e.g. the cover flow or video screen
please ask if you have any question
kind regards
Tobias
Industry/Entity Type
Restaurant
Look and feel
Each slider illustrates characteristics of the customer's brand and the style your logo design should communicate.

```html
<!DOCTYPE html>
<html lang="de">
<head>
<meta charset="utf-8">
<title>Restaurant Volmik – Kontakt</title>
<link href="https://fonts.googleapis.com/css2?family=Mulish:wght@600;700;800&display=swap" rel="stylesheet">
<style>
  :root {
    --page-bg: #1e1e1e;
    --bar-top: #6f7d2c;
    --bar-bottom: #3f4a10;
    --bar-line: #2f370b;
    --cream: #fffcc6;
    --cream-deep: #fdf7b4;
    --button-bg: #f6f3dc;
    --ink: #3b4112;
    --white: #ffffff;
    --photo-warm: #b23a2c;
    --photo-light: #efe6d6;
    --photo-dark: #5b3a24;
    --swirl: rgba(190, 180, 120, 0.18);
  }
  * { box-sizing: border-box; margin: 0; padding: 0; }
  html, body {
    width: 711px;
    height: 1200px;
    overflow: hidden;
    background: var(--page-bg);
    font-family: "Mulish", sans-serif;
  }
  .app-screen {
    position: absolute;
    left: 116px;
    top: 225px;
    width: 486px;
    height: 728px;
    background: linear-gradient(180deg, var(--cream) 0%, var(--cream-deep) 100%);
    overflow: hidden;
  }
  .nav-bar {
    position: relative;
    height: 75px;
    background: linear-gradient(180deg, var(--bar-top) 0%, var(--bar-bottom) 100%);
    border-bottom: 2px solid var(--bar-line);
  }
  .back-button {
    position: absolute;
    left: 14px;
    top: 17px;
    width: 75px;
    height: 36px;
  }
  .back-button svg { position: absolute; inset: 0; }
  .back-button span {
    position: absolute;
    left: 16px;
    top: 6px;
    width: 56px;
    text-align: center;
    font-weight: 800;
    font-size: 17px;
    color: var(--bar-bottom);
  }
  .nav-title {
    position: absolute;
    left: 0;
    right: 0;
    top: 20px;
    text-align: center;
    font-weight: 800;
    font-size: 26px;
    color: var(--white);
    letter-spacing: -0.3px;
  }
  .menu-icon {
    position: absolute;
    right: 28px;
    top: 28px;
  }
  .hero {
    position: relative;
    height: 200px;
    margin-top: 2px;
  }
  .hero-photo {
    position: absolute;
    inset: 0;
    background:
      linear-gradient(180deg, rgba(239,230,214,0.55) 0%, rgba(239,230,214,0) 45%),
      linear-gradient(90deg, var(--photo-dark) 0%, var(--photo-warm) 30%, var(--photo-light) 50%, var(--photo-warm) 72%, var(--photo-dark) 100%);
  }
  .brand-plate {
    position: absolute;
    left: 188px;
    top: 0;
    width: 124px;
    height: 96px;
    background: var(--cream);
    display: flex;
    align-items: center;
    justify-content: center;
    font-weight: 700;
    font-size: 19px;
    color: var(--bar-bottom);
  }
  .swirl-decoration {
    position: absolute;
    right: 0;
    top: 300px;
    width: 220px;
    height: 400px;
    background: radial-gradient(ellipse at 60% 40%, var(--swirl) 0%, rgba(0,0,0,0) 70%);
  }
  .contact-details {
    position: absolute;
    left: 40px;
    top: 346px;
    font-weight: 700;
    font-size: 22px;
    line-height: 33px;
    color: var(--ink);
  }
  .contact-details p + p { margin-top: 33px; }
</style>
</head>
<body>
  <main class="app-screen">
    <header class="nav-bar">
      <div class="back-button">
        <svg width="75" height="36" viewBox="0 0 75 36" aria-hidden="true">
          <path d="M14 1 H70 a4 4 0 0 1 4 4 V31 a4 4 0 0 1 -4 4 H14 L1 18 Z" fill="var(--button-bg)"/>
        </svg>
        <span>Zuruck</span>
      </div>
      <h1 class="nav-title">Kontakt</h1>
      <svg class="menu-icon" width="24" height="24" viewBox="0 0 24 24" aria-label="Menü">
        <rect x="0" y="0" width="10" height="10" fill="var(--white)"/>
        <rect x="13" y="0" width="10" height="10" fill="var(--white)"/>
        <rect x="0" y="13" width="10" height="10" fill="var(--white)"/>
        <rect x="13" y="13" width="10" height="10" fill="var(--white)"/>
      </svg>
    </header>

    <section class="hero">
      <div class="hero-photo" role="img" aria-label="Festlich gedeckter Speisesaal mit roten Stuhlhussen und Weihnachtsdekoration"></div>
      <div class="brand-plate">Volmik</div>
    </section>

    <div class="swirl-decoration" role="img" aria-label="Dezentes Rankenornament"></div>

    <section class="contact-details">
      <p>info@restaurant-volmik.ch<br>Restaurant Volmik<br>Volmikstrasse<br>6399 Seewalden/ZG</p>
      <p>T: +41 (0)41555 01 20<br>F: +41 (0)415550121</p>
      <p>Offnungszeiten<br>Taglich geoffnet</p>
    </section>
  </main>
</body>
</html>
```